Beauty Page

**UPDATED Brief**
We are looking for a website for a beauty organisation that targets both MEN & WOMAN. The focus of the company is in four main areas:

- Health
* Naturopathy & Remedial Massage
- Body
* Yoga
* Personal Training
* Massage
- Skin
* Skin care products such as Velmoracine
- Beauty
* Waxing
* Eye Treatments

We have attached the logo, (a sample of the website that I did - based on the book) and the sample of the pdf book
Updates

Dear All,

Thank you for your patience regarding the beauty contest. We were not happy with the designs that were submitted to us. We therefore had the Graphic designer to do the pricelist book to get all the colours for the organisation.

We are now happy to relaunch the contest and invite you all to take a look at the brief, download a sample of the book and the website we designed on what I’m looking for (the website is only a draft so I don’t want you to copy it) and let your creative mind go wild and present some suggestions to us.

Thanks

 

Target Market(s)

Woman & Men age 24 - 60

Industry/Entity Type

It Company

Requirements
Must have
• Use of main colours
Black
White
Gray - (CYMK - 65, 58, 57, 37)
Purpleish - Maroon (CYMK - 52, 69, 47, 25)

Use of the three color dots on the page.
(white, maroon & Gray)
Same fonts as the book
- Helvetica LT Std
Should not have
• Logo must not be altered i.e different colours, fonts, shadows etc...

```html
<!DOCTYPE html>
<html lang="en">
<head>
<meta charset="utf-8">
<title>Corvessa Beauty</title>
<link rel="stylesheet" href="https://fonts.googleapis.com/css2?family=Arimo:wght@400;700&display=swap">
<style>
:root{
  --ink:#1d1d1d;
  --text:#3a3a3a;
  --muted:#7a7a7a;
  --line:#d9d9d9;
  --paper:#ffffff;
  --page-top:#f4f4f4;
  --page-bottom:#d6d6d6;
  --gray:#5a5655;
  --gray-light:#8a8888;
  --maroon:#6e4a55;
  --green:#2f8a2f;
  --cart:#c67b1a;
}
*{box-sizing:border-box;margin:0;padding:0}
html,body{width:1200px;height:900px;overflow:hidden}
body{font-family:"Arimo",Arial,sans-serif;color:var(--text);
  background:linear-gradient(180deg,var(--page-top) 0,#ffffff 120px,#e9e9e9 500px,var(--page-bottom) 900px);position:relative}
a{text-decoration:none}
.site{position:absolute;left:236px;top:0;width:728px;height:900px}

/* header */
.header{position:relative;height:76px}
.brand{position:absolute;left:12px;top:24px;display:flex;align-items:center;gap:8px;white-space:nowrap}
.brand-mark{width:12px;height:12px;background:var(--maroon);border-radius:50%}
.brand-name{font-size:21px;font-weight:700;color:var(--ink);letter-spacing:-0.3px;line-height:1}
.nav{position:absolute;left:260px;top:8px;display:flex;height:62px;white-space:nowrap}
.nav a{display:flex;align-items:center;padding:0 8px;font-size:10px;color:var(--ink)}
.nav a.active{font-weight:700;padding:0 12px;background:linear-gradient(180deg,#ffffff,#ececec);border-left:1px solid var(--line);border-right:1px solid var(--line)}
.cart{position:absolute;left:566px;top:20px;width:158px;height:42px;border:1px solid var(--line);background:var(--paper);display:flex;align-items:center;gap:8px;padding-left:8px;white-space:nowrap}
.cart svg{width:28px;height:24px;flex:none}
.cart-title{font-size:13px;font-weight:700;color:var(--ink)}
.cart-count{font-size:9px;color:var(--muted);margin-top:2px}

/* hero */
.hero{position:absolute;top:76px;left:0;width:728px;height:234px;border-radius:8px;
  background:linear-gradient(180deg,#7b7978 0,#6a6867 55%,#595756 100%);overflow:hidden}
.hero-copy{position:absolute;left:38px;top:36px;width:380px;color:#fff;z-index:1}
.hero-title{font-size:19px;line-height:26px;font-weight:400;white-space:nowrap}
.hero-text{font-size:8.5px;line-height:12px;margin-top:12px;color:#eeeeee;width:340px}
.read-more{position:absolute;left:38px;top:160px;display:flex;height:28px;border-radius:3px;overflow:hidden;background:linear-gradient(180deg,#fff,#dedede);z-index:1}
.read-more span{padding:0 12px;font-size:10px;color:var(--ink);display:flex;align-items:center}
.read-more i{width:24px;display:flex;align-items:center;justify-content:center;border-left:1px solid #c8c8c8}
.hero-photo{position:absolute;left:420px;top:0;width:300px;height:234px;
  background:radial-gradient(ellipse at 55% 45%,#f1d9d2 0,#c9aaa4 30%,#6e6867 65%,rgba(106,104,103,0) 80%)}
.slider-tab{position:absolute;left:314px;top:296px;width:100px;height:22px;border-radius:10px 10px 0 0;background:#f2f2f2;display:flex;justify-content:center;align-items:center;gap:4px}
.slider-tab b{width:8px;height:8px;border-radius:50%;background:var(--gray-light)}
.slider-tab b.on{background:var(--maroon)}

/* main panel */
.main{position:absolute;top:318px;left:0;width:728px;height:488px;background:var(--paper);box-shadow:0 0 4px rgba(0,0,0,.08)}
.categories{position:absolute;left:16px;top:8px;width:188px}
.cat-head{height:24px;background:linear-gradient(180deg,#6e6c6b,#3f3d3c);display:flex;align-items:center;justify-content:space-between;padding:0 8px;color:#fff;font-size:15px;font-weight:700}
.cat-head i{width:14px;height:14px;border-radius:50%;background:#fff;display:flex;align-items:center;justify-content:center}
.cat-list{list-style:none;margin-top:6px}
.cat-list li{height:23px;border-bottom:1px solid var(--line);font-size:9px;color:var(--ink);display:flex;align-items:center;padding-left:12px;gap:8px}
.cat-list li::before{content:"";border-left:4px solid var(--ink);border-top:3px solid transparent;border-bottom:3px solid transparent}
.products{position:absolute;left:224px;top:8px;width:490px;display:grid;grid-template-columns:236px 236px;column-gap:14px;row-gap:22px}
.card{height:228px;border:1px solid #e4e4e4;background:var(--paper);box-shadow:0 1px 3px rgba(0,0,0,.06)}
.card-head{height:24px;display:flex;justify-content:space-between;align-items:center;padding:0 10px;background:linear-gradient(180deg,#fafafa,#ececec);border-bottom:1px solid var(--line)}
.card-title{font-size:15px;font-weight:700;color:#555}
.card-more{font-size:10px;color:var(--ink);display:flex;align-items:center;gap:5px}
.card-more::after{content:"";border-left:5px solid var(--green);border-top:4px solid transparent;border-bottom:4px solid transparent}
.card-photo{margin:14px auto 0;width:150px;height:92px;border-radius:4px;background:linear-gradient(180deg,#f7f7f7,#e3e3e6)}
.card-text{font-size:9px;line-height:12px;color:var(--ink);padding:12px 16px 0 18px}
.pager{position:absolute;right:14px;top:497px;font-size:9px;color:var(--ink);display:flex;gap:3px}
.pager .current{color:var(--green);font-weight:700}

/* partners */
.partners{position:absolute;top:828px;left:0;width:728px;height:72px;background:var(--paper);display:flex;align-items:center}
.partners-title{width:110px;margin-left:14px;text-align:center;font-size:15px;font-weight:700;color:var(--ink);line-height:18px;border-right:1px solid var(--line);height:58px;display:flex;align-items:center;justify-content:center}
.partner-list{display:flex;align-items:center;gap:40px;margin-left:36px}
.partner{font-size:18px;font-weight:700;color:#333}
.partner.accent{color:var(--green);font-size:14px}
</style>
</head>
<body>
<div class="site">
  <header class="header">
    <div class="brand"><span class="brand-mark"></span><span class="brand-name">Corvessa Beauty</span></div>
    <nav class="nav">
      <a class="active" href="#">Home</a>
      <a href="#">About Us</a>
      <a href="#">Services &amp; Treatments</a>
      <a href="#">Contact Us</a>
    </nav>
    <div class="cart">
      <svg viewBox="0 0 32 26"><path d="M1 3h5l4 14h16l4-11H8" fill="none" stroke="#c67b1a" stroke-width="2.2" stroke-linejoin="round"/><circle cx="12" cy="22" r="2.4" fill="#c67b1a"/><circle cx="24" cy="22" r="2.4" fill="#c67b1a"/></svg>
      <div><div class="cart-title">Shopping cart</div><div class="cart-count">0 item in your cart</div></div>
    </div>
  </header>

  <section class="hero">
    <div class="hero-copy">
      <h1 class="hero-title">We present people, places, traditions, cul-<br>ture and a broad overview of the incredible<br>beauty of Australia.</h1>
      <p class="hero-text">Corvessa Beauty is a health, massage skincare centre that provides quality treatments and education to each and every client to cater for all individuals.</p>
    </div>
    <a class="read-more" href="#"><span>Read more</span><i><svg width="12" height="12" viewBox="0 0 12 12"><path d="M2 4h4V1l5 5-5 5V8H2z" fill="#2f7a2f"/></svg></i></a>
    <div class="hero-photo" role="img" aria-label="Portrait of a woman in a wide striped sun hat with pink lilies"></div>
  </section>
  <div class="slider-tab"><b class="on"></b><b></b><b></b><b></b><b></b></div>

  <main class="main">
    <aside class="categories">
      <div class="cat-head">Categories <i><svg width="8" height="6" viewBox="0 0 8 6"><path d="M0 0h8L4 6z" fill="#333"/></svg></i></div>
      <ul class="cat-list">
        <li>Product name goes here</li><li>Product name goes here</li><li>Product name goes here</li><li>Product name goes here</li>
        <li>Product name goes here</li><li>Product name goes here</li><li>Product name goes here</li><li>Product name goes here</li>
        <li>Product name goes here</li><li>Product name goes here</li><li>Product name goes here</li><li>Product name goes here</li>
        <li>Product name goes here</li><li>Product name goes here</li><li>Product name goes here</li><li>Product name goes here</li>
        <li>Product name goes here</li><li>Product name goes here</li>
      </ul>
    </aside>

    <div class="products">
      <article class="card">
        <div class="card-head"><span class="card-title">Lumaris Pure</span><span class="card-more">More</span></div>
        <div class="card-photo" role="img" aria-label="Range of white and blue skincare tubes and jars"></div>
        <p class="card-text">Lorem Ipsum is simply dummy text of the printing and typesetting industry. Lorem Ipsum has Quillset Composer including versions of Lorem Ipsum.</p>
      </article>
      <article class="card">
        <div class="card-head"><span class="card-title">Opaline White</span><span class="card-more">More</span></div>
        <div class="card-photo" role="img" aria-label="Set of white skincare bottles and boxes"></div>
        <p class="card-text">Lorem Ipsum is simply dummy text of the printing and typesetting industry. Lorem Ipsum has Quillset Composer including versions of Lorem Ipsum.</p>
      </article>
      <article class="card">
        <div class="card-head"><span class="card-title">Veridex Clearing</span><span class="card-more">More</span></div>
        <div class="card-photo" role="img" aria-label="Collection of dark and white skincare bottles"></div>
        <p class="card-text">Lorem Ipsum is simply dummy text of the printing and typesetting industry. Lorem Ipsum has Quillset Composer including versions of Lorem Ipsum.</p>
      </article>
      <article class="card">
        <div class="card-head"><span class="card-title">Fresh Ground</span><span class="card-more">More</span></div>
        <div class="card-photo" role="img" aria-label="Colourful cleansing bottles and a spray pump"></div>
        <p class="card-text">Lorem Ipsum is simply dummy text of the printing and typesetting industry. Lorem Ipsum has Quillset Composer including versions of Lorem Ipsum.</p>
      </article>
    </div>

    <nav class="pager"><span>Prev</span><span class="current">1</span><span>2</span><span>3</span><span>4</span><span>5</span><span>Next</span></nav>
  </main>

  <footer class="partners">
    <div class="partners-title">OUR<br>PATNERS</div>
    <div class="partner-list">
      <span class="partner">Aurelline</span>
      <span class="partner">Velmoracine</span>
      <span class="partner">Aurelline</span>
      <span class="partner accent">Sorvane Peel</span>
    </div>
  </footer>
</div>
</body>
</html>
```